Our swimming pool service needs your help with letterhead

Letterhead for small swimming pool service- We would like a professional look with a creative layout- must be compatible with LedgerNest forms (sample attached)
No more than 2 colors in graphics

Target Market(s)

Homeowners/ Contractors

Font styles to use
Sans Serif

Colors
33a6d7
85cae6

Requirements
Must have
• Logo (file attached)
• Compatible with LedgerNest (sample attached)
• Mailing address- P.O. Box 58, Cedar Hollow NY 11592
• phone- (631) 529-6180
• email- marcdoylewater@mailbrook.net
• Licensed & Insured
Nice to have
• Small slogan- Examples:Family owned and operated for 25 years, 25 years of trusted service
• Creative layout
Should not have
• Blue color must be same as blue in our logo
• No thick lines of color
• No design in middle of page

```html
<!DOCTYPE html>
<html lang="en">
<head>
<meta charset="utf-8">
<title>Marc T. Doyle Pool Service – Invoice Letterhead</title>
<link rel="stylesheet" href="https://fonts.googleapis.com/css2?family=Source+Sans+3:wght@400;600&family=Roboto:wght@400&display=swap">
<style>
  :root {
    --navy: #0b2070;
    --sky: #66ccff;
    --sky-soft: rgba(102, 204, 255, 0);
    --sky-text: #5cc6f6;
    --cell: #e3f4fd;
    --paper: #ffffff;
  }
  * { box-sizing: border-box; margin: 0; padding: 0; }
  html, body { width: 928px; height: 1200px; overflow: hidden; background: var(--paper); }
  .sheet {
    position: relative; width: 928px; height: 1200px; overflow: hidden;
    border: 1px solid #111; background: var(--paper);
    font-family: "Source Sans 3", sans-serif; color: var(--navy);
  }
  .abs { position: absolute; }

  .corner-accent { position: absolute; }
  .corner-accent.top-right {
    left: 644px; top: 0; width: 284px; height: 140px;
    background: radial-gradient(ellipse at 100% 0%, var(--sky) 0%, var(--sky-soft) 75%);
  }
  .corner-accent.bottom-left {
    left: 0; top: 1054px; width: 284px; height: 146px;
    background: radial-gradient(ellipse at 0% 100%, var(--sky) 0%, var(--sky-soft) 75%);
  }

  .brand { left: 69px; top: 72px; display: flex; align-items: center; gap: 10px; }
  .brand-mark { width: 34px; height: 34px; border-radius: 50%; background: var(--sky); margin-top: 26px; }
  .brand-name { font-weight: 600; color: var(--navy); line-height: 1; }
  .brand-name .owner { display: block; font-size: 21px; letter-spacing: 2px; text-align: center; }
  .brand-name .trade { display: block; font-size: 38px; letter-spacing: 1px; margin-top: 4px; }

  .address { left: 526px; top: 164px; font-size: 33px; line-height: 43px; font-weight: 400; }
  .contact { left: 526px; font-family: "Roboto", sans-serif; color: var(--sky-text); font-size: 22px; display: flex; align-items: center; gap: 14px; white-space: nowrap; }
  .contact.phone { top: 268px; }
  .contact.email { top: 297px; }
  .contact svg { flex: none; }

  .cell { position: absolute; background: var(--cell); font-size: 16px; display: flex; align-items: center; justify-content: center; }
  .bill-head { left: 74px; top: 246px; width: 367px; height: 27px; }
  .bill-body { left: 74px; top: 278px; width: 367px; height: 147px; }

  .note { left: 74px; top: 882px; font-size: 19px; line-height: 25px; }

  .footer-band { position: absolute; left: 0; top: 1149px; }
  .footer-band path { fill: var(--navy); }
  .slogan { left: 380px; top: 1162px; color: #fff; font-size: 18px; white-space: nowrap; }
</style>
</head>
<body>
<div class="sheet">

  <div class="corner-accent top-right" role="img" aria-label="Light blue water accent in the top right corner"></div>

  <div class="abs brand">
    <div class="brand-mark"></div>
    <div class="brand-name">
      <span class="owner">— MARC T. DOYLE —</span>
      <span class="trade">POOL SERVICE</span>
    </div>
  </div>

  <div class="abs address">P.O. Box 58,<br>Cedar Hollow NY 11592</div>

  <div class="abs contact phone">
    <svg width="18" height="28" viewBox="0 0 18 28" aria-hidden="true">
      <rect x="1" y="1" width="16" height="26" rx="3" fill="var(--sky)"/>
      <rect x="3.5" y="4" width="11" height="16" fill="#fff"/>
      <rect x="7" y="22" width="4" height="3" fill="#fff"/>
    </svg>
    <span>(631) 529-6180</span>
  </div>
  <div class="abs contact email">
    <svg width="22" height="16" viewBox="0 0 22 16" aria-hidden="true">
      <rect x="0" y="1" width="22" height="14" fill="var(--sky)"/>
      <path d="M0,1 L11,9 L22,1 M0,15 L8,7 M22,15 L14,7" stroke="#fff" stroke-width="1.5" fill="none"/>
    </svg>
    <span>marcdoylewater@mailbrook.net</span>
  </div>

  <div class="cell bill-head">BILL TO:</div>
  <div class="cell bill-body"></div>

  <div class="cell" style="left:73px;top:491px;width:155px;height:27px;">DATE</div>
  <div class="cell" style="left:73px;top:521px;width:155px;height:26px;">9/11/2019</div>
  <div class="cell" style="left:556px;top:492px;width:153px;height:27px;">INVOICE</div>
  <div class="cell" style="left:712px;top:491px;width:144px;height:27px;">TERMS</div>
  <div class="cell" style="left:556px;top:522px;width:153px;height:25px;"></div>
  <div class="cell" style="left:712px;top:521px;width:144px;height:26px;"></div>

  <div class="cell" style="left:73px;top:550px;width:481px;height:27px;">DESCRIPTION</div>
  <div class="cell" style="left:556px;top:550px;width:53px;height:27px;">QTY</div>
  <div class="cell" style="left:611px;top:550px;width:99px;height:27px;">RATE</div>
  <div class="cell" style="left:712px;top:550px;width:144px;height:27px;">AMOUNT</div>

  <div class="cell" style="left:73px;top:579px;width:481px;height:27px;"></div><div class="cell" style="left:556px;top:579px;width:53px;height:27px;"></div><div class="cell" style="left:611px;top:579px;width:99px;height:27px;"></div><div class="cell" style="left:712px;top:579px;width:144px;height:27px;"></div>
  <div class="cell" style="left:73px;top:609px;width:481px;height:27px;"></div><div class="cell" style="left:556px;top:609px;width:53px;height:27px;"></div><div class="cell" style="left:611px;top:609px;width:99px;height:27px;"></div><div class="cell" style="left:712px;top:609px;width:144px;height:27px;"></div>
  <div class="cell" style="left:73px;top:638px;width:481px;height:27px;"></div><div class="cell" style="left:556px;top:638px;width:53px;height:27px;"></div><div class="cell" style="left:611px;top:638px;width:99px;height:27px;"></div><div class="cell" style="left:712px;top:638px;width:144px;height:27px;"></div>
  <div class="cell" style="left:73px;top:668px;width:481px;height:27px;"></div><div class="cell" style="left:556px;top:668px;width:53px;height:27px;"></div><div class="cell" style="left:611px;top:668px;width:99px;height:27px;"></div><div class="cell" style="left:712px;top:668px;width:144px;height:27px;"></div>
  <div class="cell" style="left:73px;top:698px;width:481px;height:27px;"></div><div class="cell" style="left:556px;top:698px;width:53px;height:27px;"></div><div class="cell" style="left:611px;top:698px;width:99px;height:27px;"></div><div class="cell" style="left:712px;top:698px;width:144px;height:27px;"></div>
  <div class="cell" style="left:73px;top:727px;width:481px;height:27px;"></div><div class="cell" style="left:556px;top:727px;width:53px;height:27px;"></div><div class="cell" style="left:611px;top:727px;width:99px;height:27px;"></div><div class="cell" style="left:712px;top:727px;width:144px;height:27px;"></div>
  <div class="cell" style="left:73px;top:757px;width:481px;height:27px;"></div><div class="cell" style="left:556px;top:757px;width:53px;height:27px;"></div><div class="cell" style="left:611px;top:757px;width:99px;height:27px;"></div><div class="cell" style="left:712px;top:757px;width:144px;height:27px;"></div>
  <div class="cell" style="left:73px;top:786px;width:481px;height:27px;"></div><div class="cell" style="left:556px;top:786px;width:53px;height:27px;"></div><div class="cell" style="left:611px;top:786px;width:99px;height:27px;"></div><div class="cell" style="left:712px;top:786px;width:144px;height:27px;"></div>
  <div class="cell" style="left:73px;top:815px;width:481px;height:27px;"></div><div class="cell" style="left:556px;top:815px;width:53px;height:27px;"></div><div class="cell" style="left:611px;top:815px;width:99px;height:27px;"></div><div class="cell" style="left:712px;top:815px;width:144px;height:27px;"></div>
  <div class="cell" style="left:73px;top:845px;width:481px;height:26px;"></div><div class="cell" style="left:556px;top:845px;width:53px;height:26px;"></div><div class="cell" style="left:611px;top:845px;width:99px;height:26px;"></div><div class="cell" style="left:712px;top:845px;width:144px;height:26px;"></div>

  <div class="cell" style="left:611px;top:873px;width:245px;height:26px;justify-content:flex-start;padding-left:25px;">TOTAL</div>

  <div class="abs note">CHECK PAY BILL TO MARC T. DOYLE.<br>CHARGE BY PHONE.</div>

  <div class="corner-accent bottom-left" role="img" aria-label="Light blue water accent in the bottom left corner"></div>

  <svg class="footer-band" width="928" height="51" viewBox="0 0 928 51" aria-hidden="true">
    <path d="M385,0 L928,0 L928,51 L308,51Z"/>
  </svg>
  <div class="abs slogan">Family owned and operated for 25 years, 25 years of trusted service</div>

</div>
</body>
</html>
```